Clinical Hypnotherapist needs business card design

I need a business card design that gives the impression of being approachable yet professional. As a clinical hypnotherapist I need to create trust from my clients to allow me access to their inner mind to enable them to make changes and to start to live the life that they want to live. My website is www.lunarelle.com.au and I would like my business cards to reflect my website. I would like a space for appointment details on the back of the card.

```html
<!DOCTYPE html>
<html lang="en">
<head>
<meta charset="utf-8">
<title>Elise Carrow – Clinical Hypnotherapist Business Card</title>
<link rel="stylesheet" href="https://fonts.googleapis.com/css2?family=Lato:wght@400;700;900&family=Michroma&display=swap">
<style>
  :root {
    --plum: #7b1470;
    --plum-dark: #6a0f60;
    --ink: #1c1c1c;
    --text: #3a3a3a;
    --card: #ffffff;
    --backdrop: #2b2b2b;
    --photo-top: #8f9aa3;
    --photo-bottom: #c8663f;
  }
  * { box-sizing: border-box; margin: 0; padding: 0; }
  html, body { width: 1200px; height: 975px; overflow: hidden; }
  body {
    background: var(--backdrop);
    font-family: "Lato", sans-serif;
    position: relative;
  }
  .card {
    position: absolute;
    width: 700px;
    height: 428px;
    background: var(--card);
    border-radius: 22px;
    overflow: hidden;
    box-shadow: 0 14px 40px rgba(0,0,0,.45);
  }
  .card--back { left: 120px; top: 40px; }
  .card--front { left: 380px; top: 505px; }

  /* ---------- back: appointment card ---------- */
  .appt-label {
    position: absolute; left: 40px; top: 44px;
    background: var(--plum); color: #fff;
    font-weight: 900; font-size: 19px; letter-spacing: .5px;
    padding: 5px 12px; border-radius: 3px;
  }
  .back-title {
    position: absolute; right: 60px; top: 34px;
    font-family: "Michroma", sans-serif; color: var(--plum);
    font-size: 17px; line-height: 1.15; text-align: center;
  }
  .form-row {
    position: absolute; left: 40px; right: 40px;
    display: flex; align-items: flex-end; gap: 10px;
    color: var(--text); font-size: 17px; font-weight: 700;
  }
  .form-row .line { flex: 1; border-bottom: 2px dotted #555; height: 1px; margin-bottom: 4px; }
  .form-row--date { top: 122px; }
  .form-row--therapist { top: 248px; }
  .checkbox {
    display: inline-block; width: 24px; height: 22px;
    border: 2px solid var(--plum); border-radius: 5px; vertical-align: middle;
  }
  .ampm { display: flex; gap: 10px; align-items: center; font-size: 14px; }
  .days {
    position: absolute; left: 40px; right: 40px; top: 182px;
    display: flex; justify-content: space-between;
    font-weight: 900; font-size: 18px; color: var(--ink);
  }
  .days span { display: flex; align-items: center; gap: 6px; }
  .policy {
    position: absolute; left: 0; right: 0; top: 300px; text-align: center;
  }
  .policy-label {
    display: inline-block; background: var(--plum); color: #fff;
    font-weight: 900; font-size: 14px; letter-spacing: .5px;
    padding: 3px 12px; border-radius: 4px;
  }
  .policy-text {
    margin-top: 10px; color: var(--text);
    font-weight: 700; font-size: 16px; line-height: 1.35;
  }

  /* ---------- front ---------- */
  .front-title {
    position: absolute; right: 250px; top: 38px;
    font-family: "Michroma", sans-serif; color: var(--plum);
    font-size: 19px; letter-spacing: .2px; white-space: nowrap;
  }
  .tagline {
    position: absolute; right: 245px; top: 68px;
    background: var(--plum); color: #fff;
    font-family: "Michroma", sans-serif; font-size: 10.5px;
    padding: 4px 10px; border-radius: 5px; white-space: nowrap;
  }
  .accent-strip {
    position: absolute; right: 0; top: 62px; width: 60px; height: 90px;
    background: var(--plum);
  }
  .name-band {
    position: absolute; left: 0; top: 100px; width: 470px; height: 170px;
    background: var(--plum);
  }
  .identity {
    position: absolute; left: 40px; top: 122px; color: #fff;
  }
  .identity .name { font-weight: 900; font-size: 34px; letter-spacing: .5px; line-height: 1.1; }
  .identity .role { font-weight: 700; font-size: 18px; margin-top: 2px; }
  .identity .phone { font-weight: 700; font-size: 40px; line-height: 1.15; letter-spacing: 1px; }
  .portrait {
    position: absolute; left: 480px; top: 52px; width: 190px; height: 180px;
    border-radius: 14px; border: 3px solid #fff;
    background: linear-gradient(180deg, var(--photo-top) 0%, #a9a9a9 45%, var(--photo-bottom) 100%);
    box-shadow: 0 2px 8px rgba(0,0,0,.25);
  }
  .services-heading {
    position: absolute; left: 330px; top: 292px;
    font-weight: 900; font-size: 20px; letter-spacing: 4px; color: var(--ink);
  }
  .services {
    position: absolute; left: 40px; right: 30px; top: 324px;
    color: var(--plum); font-weight: 700; font-size: 20px; line-height: 1.45;
    text-align: right;
  }
</style>
</head>
<body>

<section class="card card--back" aria-label="Appointment card, back">
  <div class="appt-label">NEXT APPOINTMENT</div>
  <div class="back-title">CLINICAL<br>HYPNOTHERAPIST</div>

  <div class="form-row form-row--date">
    <span>DATE:</span><span class="line"></span>
    <span>TIME:</span><span class="line"></span>
    <span class="ampm">AM <i class="checkbox"></i> PM <i class="checkbox"></i></span>
  </div>

  <div class="days">
    <span>Mon <i class="checkbox"></i></span>
    <span>Tue <i class="checkbox"></i></span>
    <span>Wed <i class="checkbox"></i></span>
    <span>Thu <i class="checkbox"></i></span>
    <span>Fri <i class="checkbox"></i></span>
    <span>Sat <i class="checkbox"></i></span>
    <span>Sun <i class="checkbox"></i></span>
  </div>

  <div class="form-row form-row--therapist">
    <span>NAME OF THERAPIST:</span><span class="line"></span>
  </div>

  <div class="policy">
    <span class="policy-label">CANCELLATION POLICY</span>
    <p class="policy-text">Minimum of 24hrs notice is required prior to appointment time<br>or you will be charged $25 for the service.</p>
  </div>
</section>

<section class="card card--front" aria-label="Business card, front">
  <h1 class="front-title">CLINICAL HYPNOTHERAPIST</h1>
  <div class="tagline">GAIN CONTROL OF YOUR LIFE WITH HYPNOTHERAPY</div>
  <div class="accent-strip"></div>
  <div class="name-band"></div>
  <div class="identity">
    <div class="name">ELISE CARROW</div>
    <div class="role">Brisbane Hypnotherapist</div>
    <div class="phone">0412 555 019</div>
  </div>
  <div class="portrait" role="img" aria-label="Portrait photograph of the hypnotherapist"></div>
  <h2 class="services-heading">OUR SERVICES</h2>
  <p class="services">
    Stop Smoking / Depression / Usui Reiki / Past Life Regression<br>
    Weight Control / Confidence / Anxiety &amp; Stress / Counselling
  </p>
</section>

</body>
</html>
```